Harborline Washtek Laundry Service Company

I own a Coin Operated laundry business and need to include a picture of Coin operated machines.
Include:
Company Name: Harborline Washtek
For all your Coin Operated Laundry needs.Include: sales, service, and new installations with commissions as high as 50%
include 1187 N. Larkview Rd, Arcadia, Ca 90417
626-518-2790
Include: Contact: Dwight Menser

Target Market(s)

coin Laundry

Industry/Entity Type

Business

Requirements
Must have
• picture of machines
• Sales, Service, Installations

```html
<!DOCTYPE html>
<html lang="en">
<head>
<meta charset="utf-8">
<title>Harborline Washtek Laundry Service – Postcard</title>
<link rel="stylesheet" href="https://fonts.googleapis.com/css2?family=Crimson+Pro:wght@500;600;700&family=Roboto+Condensed:wght@400;700&family=Oswald:wght@500;600&family=Arimo:wght@400&display=swap">
<style>
  :root{
    --bg:#7a5a3c;
    --orange:#f26a21;
    --blue:#1677c8;
    --blue-deep:#0d5fa8;
    --sky:#2aa6e6;
    --yellow:#ffe83a;
    --ink:#333a44;
    --grey-1:#f4f5f6;
    --white:#ffffff;
  }
  *{box-sizing:border-box;margin:0;padding:0}
  html,body{width:907px;height:1200px;overflow:hidden}
  body{background:var(--bg);position:relative;font-family:"Crimson Pro",serif;color:var(--ink)}

  .card{position:absolute;overflow:hidden;background:var(--grey-1);box-shadow:0 6px 14px rgba(0,0,0,.35)}
  .card-front{left:85px;top:62px;width:741px;height:483px}
  .card-back{left:85px;top:622px;width:747px;height:482px}
  .card-bg{position:absolute;inset:0;width:100%;height:100%}

  .photo{position:absolute}
  .photo-machine{left:15px;top:62px;width:284px;height:402px;border-radius:4px;
    background:linear-gradient(100deg,#e3e6e9 0%,#ffffff 45%,#d3d7dc 100%)}

  .brand{position:absolute;text-align:center}
  .brand-name{font-weight:700;color:var(--orange);letter-spacing:.2px;white-space:nowrap;line-height:1}
  .brand-tag{display:flex;align-items:center;gap:8px;font-weight:500;color:var(--ink);letter-spacing:.6px;white-space:nowrap}
  .brand-tag::before,.brand-tag::after{content:"";flex:1;height:1px;background:var(--ink)}

  .front-brand{left:370px;top:20px;width:298px}
  .front-brand .brand-name{font-size:28px}
  .front-brand .brand-tag{font-size:15px;margin-top:6px}
  .front-rule{position:absolute;left:335px;top:84px;width:370px;height:3px;background:var(--orange)}

  .headline{position:absolute;left:336px;top:96px;font-family:"Roboto Condensed",sans-serif;font-weight:700;
    font-size:62px;line-height:1;color:var(--blue);letter-spacing:0;white-space:nowrap;text-shadow:0 3px 4px rgba(0,0,0,.3)}
  .ribbon{position:absolute;font-family:"Roboto Condensed",sans-serif;color:var(--white);font-size:40px;line-height:1}
  .ribbon-orange{left:400px;top:166px;width:341px;height:57px;background:var(--orange);
    clip-path:polygon(8% 0,100% 0,100% 100%,0 100%);padding:9px 0 0 42px}
  .ribbon-blue{left:300px;top:231px;width:311px;height:54px;background:var(--blue);
    clip-path:polygon(0 0,100% 0,92% 100%,0 100%);padding:8px 0 0 45px}

  .offer{font-size:24px;line-height:27px;font-weight:500;white-space:nowrap}
  .front-offer{position:absolute;left:346px;top:294px;color:var(--ink)}
  .front-offer em{font-style:normal;color:var(--blue)}

  .call{position:absolute;left:432px;top:422px;font-family:"Oswald",sans-serif;font-weight:600;font-size:31px;
    color:var(--white);text-shadow:0 2px 3px rgba(0,0,0,.35);white-space:nowrap}
  .call .number{color:var(--yellow);margin-left:8px}

  .photo-laundry{left:0;top:0;width:480px;height:175px;
    background:linear-gradient(180deg,rgba(200,190,182,.9) 0%,rgba(225,225,228,.7) 60%,rgba(244,245,246,0) 100%)}
  .postage{position:absolute;left:627px;top:14px;width:106px;height:105px;border:1.5px solid #222;background:var(--white);
    font-family:"Arimo",sans-serif;font-size:13px;line-height:16px;text-align:center;padding-top:34px;color:#111}
  .back-brand{left:19px;top:136px;width:320px}
  .back-brand .brand-name{font-size:30px}
  .back-brand .brand-tag{font-size:16px;margin-top:6px}

  .contact-name{position:absolute;left:34px;top:210px;width:156px;height:33px;border-radius:8px;background:var(--blue);
    color:var(--white);font-family:"Roboto Condensed",sans-serif;font-weight:700;font-size:19px;letter-spacing:.5px;
    text-align:center;line-height:33px}
  .contact-line{position:absolute;left:40px;display:flex;align-items:center;gap:16px;
    font-family:"Roboto Condensed",sans-serif;font-weight:700;font-size:19px;color:#2a2f36;white-space:nowrap}
  .contact-line svg{width:20px;height:22px;fill:var(--blue)}
  .contact-phone{top:267px}
  .contact-address{top:309px}

  .offer-band{position:absolute;left:0;top:345px;width:497px;height:69px;background:var(--orange);color:var(--white);
    padding:7px 0 0 44px}

  .address-panel{position:absolute;left:497px;top:210px;width:250px;height:272px;background:var(--white)}
  .address-label{position:absolute;left:24px;top:21px;font-family:"Arimo",sans-serif;font-size:13px;color:#111}
  .address-line{position:absolute;left:23px;width:191px;height:1px;background:#222}
</style>
</head>
<body>

<section class="card card-front" aria-label="Postcard front">
  <svg class="card-bg" viewBox="0 0 741 483" preserveAspectRatio="none" aria-hidden="true">
    <path d="M0 0 H741 V483 H0Z" fill="#f1f2f3"/>
    <path d="M120 0 C260 140 420 180 741 150 V0Z" fill="#e4e6e9"/>
    <path d="M0 300 C200 200 500 330 741 230 V260 C520 360 220 250 0 340Z" fill="#e8eaec"/>
    <path d="M300 400 C470 430 650 390 741 300 V483 H300Z" fill="var(--orange)"/>
    <path d="M0 400 C120 395 250 420 360 395 C520 430 660 410 741 340 V483 H0Z" fill="var(--sky)"/>
    <path d="M0 420 C200 430 380 420 520 420 C620 420 700 400 741 370 V483 H0Z" fill="var(--blue-deep)"/>
  </svg>
  <div class="photo photo-machine" role="img" aria-label="Photo of a white front-loading coin-operated washing machine"></div>

  <div class="brand front-brand">
    <div class="brand-name">HARBORLINE WASHTEK</div>
    <div class="brand-tag">LAUNDRY SERVICE</div>
  </div>
  <div class="front-rule"></div>

  <h1 class="headline">FOR ALL YOUR</h1>
  <div class="ribbon ribbon-orange">Coin Operated</div>
  <div class="ribbon ribbon-blue">Laundry needs</div>

  <p class="offer front-offer">Sales, Service, &amp; New Installations<br>with commissions as high as <em>50%</em></p>

  <p class="call">Call Us <span class="number">626-518-2790</span></p>
</section>

<section class="card card-back" aria-label="Postcard back">
  <svg class="card-bg" viewBox="0 0 747 482" preserveAspectRatio="none" aria-hidden="true">
    <path d="M0 0 H747 V482 H0Z" fill="#f3f4f5"/>
    <path d="M300 0 C420 120 560 180 747 190 V0Z" fill="#e2e5e8"/>
    <path d="M380 0 C470 90 600 140 747 150 V170 C590 160 450 110 360 0Z" fill="#d4d8dc"/>
    <path d="M0 200 C120 180 260 240 497 220 V250 C260 270 120 210 0 230Z" fill="#e6e8ea"/>
    <path d="M0 414 H497 V482 H0Z" fill="#ffffff"/>
    <path d="M0 430 C150 450 300 470 497 440 V482 H0Z" fill="#eceef0"/>
  </svg>
  <div class="photo photo-laundry" role="img" aria-label="Photo of a woman loading clothes into a laundromat washer"></div>
  <div class="postage">Postage<br>Area</div>

  <div class="brand back-brand">
    <div class="brand-name">HARBORLINE WASHTEK</div>
    <div class="brand-tag">LAUNDRY SERVICE</div>
  </div>

  <div class="contact-name">DWIGHT MENSER</div>
  <p class="contact-line contact-phone">
    <svg viewBox="0 0 24 24" aria-hidden="true"><path d="M6.6 2.5c.6-.4 1.4-.2 1.8.4l2 3.2c.4.6.3 1.4-.3 1.8l-1.5 1.1c.9 2.1 2.4 3.9 4.3 5.2l1.3-1.4c.5-.5 1.3-.6 1.8-.1l3 2.4c.6.5.7 1.3.2 1.9l-1.6 2c-.8 1-2.2 1.300-3.4.8C8.8 17.6 5.2 13.3 3.8 8.3c-.3-1.2.1-2.5 1.1-3.2z"/></svg>
    626-518-2790
  </p>
  <p class="contact-line contact-address">
    <svg viewBox="0 0 24 24" aria-hidden="true"><path d="M12 1.5a7 7 0 0 0-7 7c0 5.2 7 14 7 14s7-8.8 7-14a7 7 0 0 0-7-7zm0 9.8a2.8 2.8 0 1 1 0-5.6 2.8 2.8 0 0 1 0 5.6z"/></svg>
    1187 N. Larkview Rd, Arcadia, Ca 90417.
  </p>

  <p class="offer offer-band">Sales, Service, &amp; New Installations<br>with commissions as high as 50%</p>

  <div class="address-panel">
    <span class="address-label">Address</span>
    <span class="address-line" style="top:73px"></span>
    <span class="address-line" style="top:108px"></span>
    <span class="address-line" style="top:143px"></span>
    <span class="address-line" style="top:178px"></span>
  </div>
</section>

</body>
</html>
```